Harlow Ironworks Business Card

We need a business card design for a new small metal fabrication business in rural NSW, Australia.

The business (Harlow Ironworks) is owner operated by a man with the initials KB - much of the branding comes from this name.

Harlow Ironworks designs, engineers, repairs and manufactures a range of custom, quality metal works including vehicle trays, agricultural machinery impliments, trailers, wood splitters, fire pits, furniture etc.

The brand position focuses on custom work of the highest quality.

Business card design should show quality, attention to detail and stand out among a mass of business cards.

Logos are in the files

The grey color may be changed on the logo if required to stand out more.

There is an image attached of a simple card that is liked because it is clean, clear, simple, masculine and effective. It says 'quality'. As most of the work we do is custom it would be good to have the business card speak to this.

Target Market(s)

Rural and regional based Australians. Primarily adult male 25-60 yrs. Primary production / rural / travelling lifestyle.

Industry/Entity Type

Metal Fabrication

Contact Information for Business Card

The words 'custom quality fabrications' would be great somewhere perhaps on the backside (not on the information side)
Name
title
Phone: 0418 539 746 and (02) 6193 4827
email: info@harlowiw.com.au
www.harlowiw.com.au

address (2 lines)

Requirements
Nice to have
• Background colour should be very navy blue or black.
Should not have
• NO orange and blue combinations.
• Navy is OK

```html
<!DOCTYPE html>
<html lang="en">
<head>
<meta charset="utf-8">
<title>Harlow Ironworks – Business Card, Variation 1 Portrait</title>
<link rel="stylesheet" href="https://fonts.googleapis.com/css2?family=Lato:ital,wght@0,300;0,400;0,700;0,900;1,400&display=swap">
<style>
  :root {
    --board: #dcdcdc;
    --navy: #02113a;
    --green: #5db543;
    --steel: #a2a2a2;
    --label: #6f6f6f;
    --ink: #1a1a1a;
    --title-grey: #555555;
    --paper: #ffffff;
  }
  * { box-sizing: border-box; margin: 0; padding: 0; }
  html, body { width: 1200px; height: 1200px; overflow: hidden; }
  body {
    position: relative;
    background: var(--board);
    font-family: "Lato", sans-serif;
  }

  .board-title {
    position: absolute; left: 116px; top: 16px;
    font-size: 52px; letter-spacing: -0.5px; line-height: 1.1;
    color: var(--title-grey); font-weight: 900;
  }
  .board-title em { font-style: italic; font-weight: 400; color: var(--ink); }

  .swatches { position: absolute; left: 5px; top: 107px; width: 45px; }
  .swatch { height: 46px; }
  .swatch--navy { background: var(--navy); }
  .swatch--green { background: var(--green); }
  .swatch--steel { background: var(--steel); }

  .side-label {
    position: absolute; top: 120px;
    font-size: 56px; font-weight: 300; color: var(--label);
  }
  .side-label--top { left: 114px; }
  .side-label--info { left: 648px; }

  .dimension {
    position: absolute; font-size: 50px; font-weight: 300; color: var(--label);
    white-space: nowrap;
  }
  .dimension--height {
    left: 74px; top: 552px;
    transform: translate(-50%, -50%) rotate(-90deg);
  }
  .dimension--width { left: 278px; top: 1100px; }

  .card {
    position: absolute; top: 218px; width: 489px; height: 856px;
    box-shadow: 28px 34px 26px rgba(0,0,0,0.38);
  }
  .card--front { left: 114px; background: var(--navy); }
  .card--info { left: 653px; background: var(--paper); }

  .card__frame {
    position: absolute; left: 18px; top: 22px; right: 18px; bottom: 18px;
    border: 2px solid var(--green);
    z-index: 2;
  }

  .front__brand {
    position: absolute; left: 0; right: 0; top: 250px;
    text-align: center; color: var(--steel);
    font-weight: 900; font-size: 50px; line-height: 1.05; letter-spacing: 3px;
  }
  .front__pattern {
    position: absolute; left: 20px; right: 20px; top: 486px; bottom: 41px;
    background: radial-gradient(ellipse at 40% 45%, #0c1d4a 0%, var(--navy) 75%);
  }
  .front__tagline {
    position: absolute; left: 18px; right: 18px; bottom: 18px; height: 23px;
    background: var(--green); color: var(--paper);
    font-style: italic; font-size: 18px; line-height: 23px; text-align: center;
    z-index: 3;
  }

  .info__brand {
    position: absolute; left: 0; right: 0; top: 120px;
    text-align: center; color: var(--steel);
    font-weight: 900; font-size: 30px; line-height: 1.05; letter-spacing: 2px;
  }
  .info__name {
    position: absolute; left: 0; right: 0; top: 324px;
    text-align: center; font-size: 38px; font-weight: 300; color: var(--ink);
  }
  .info__role {
    position: absolute; left: 0; right: 0; top: 390px;
    text-align: center; font-size: 26px; font-weight: 700; color: #666;
  }
  .info__contact {
    position: absolute; left: 40px; right: 40px; top: 440px;
    text-align: center; font-size: 28px; font-weight: 300; line-height: 37px; color: var(--ink);
  }
  .info__pattern {
    position: absolute; left: 20px; right: 20px; top: 658px; bottom: 20px;
    background: radial-gradient(ellipse at 45% 55%, #f1f1f1 0%, var(--paper) 75%);
  }
</style>
</head>
<body>
  <h1 class="board-title">VARIATION 1: <em>Portrait</em></h1>

  <div class="swatches" aria-label="Colour palette">
    <div class="swatch swatch--navy"></div>
    <div class="swatch swatch--green"></div>
    <div class="swatch swatch--steel"></div>
  </div>

  <p class="side-label side-label--top">Top Side</p>
  <p class="side-label side-label--info">Info Side</p>

  <p class="dimension dimension--height">88.9mm</p>
  <p class="dimension dimension--width">50.8mm</p>

  <section class="card card--front" aria-label="Card front">
    <div class="front__pattern" role="img" aria-label="Faint line drawing of interlocking machine gears"></div>
    <div class="card__frame"></div>
    <p class="front__brand">HARLOW<br>IRONWORKS</p>
    <p class="front__tagline">Custom quality fabrications</p>
  </section>

  <section class="card card--info" aria-label="Card info side">
    <div class="info__pattern" role="img" aria-label="Very faint line drawing of machine gears"></div>
    <div class="card__frame"></div>
    <p class="info__brand">HARLOW<br>IRONWORKS</p>
    <p class="info__name">HARLOW KB</p>
    <p class="info__role">Managing Director</p>
    <p class="info__contact">
      Phone: 0418 539 746 and (02)<br>
      6193 4827<br>
      email: info@harlowiw.com.au<br>
      www.harlowiw.com.au
    </p>
  </section>
</body>
</html>
```